Flyer & Business Card for Lakeside Lens Guild photography courses

I need a flyer design for my company Lakeside Lens Guild - which offers photography classes for all levels in Geneva / Switzerland.

The flyer has to have an attractive visual at the front, and should highlight different types of classes and our teaching philosophy in the back.

Especially the images of Geneva (you can find some on lakesidelensguild.com and also on my photography website www.morvakimagery.com) will help to make people appreciate it's local.

Please check my website to learn more about my company, the logo, brand identity and the overall feeling:
https://www.lakesidelensguild.com

For the colors, I have used blue in the website and the logo, so it should be somehow compatible.

The final design should communicate fun courses offered by professional photographers that have received consistently 5 star ratings.

Target Market(s)

Geneva / Switzerland

Industry/Entity Type

Business

Contact Information for Business Card

Double sided - front could be a photo (or multiple photos that could be printed as part of one order from pex.com) and the back should communicate the brand identity.

Colors
0292cd
33a6d7
0555a3

```html
<!DOCTYPE html>
<html lang="en">
<head>
<meta charset="utf-8">
<title>Lakeside Lens Guild – Flyer</title>
<link href="https://fonts.googleapis.com/css2?family=Open+Sans:ital,wght@0,400;0,600;0,700;1,600;1,700&family=Poppins:ital,wght@0,500;0,600;0,700;1,500&display=swap" rel="stylesheet">
<style>
:root{
  --stage:#f4f1ea;
  --ink-dark:#0c1a26;
  --navy:#0f2a4d;
  --deep-blue:#0555a3;
  --brand-blue:#0292cd;
  --light-blue:#33a6d7;
  --sky:#4fa9e0;
  --teal-dark:#163a4c;
  --slate:#5a6670;
  --accent-orange:#f07a2a;
  --white:#ffffff;
  --card-bg:#ffffff;
  --card-text:#333;
  --btn:#3a3fb0;
}
*{margin:0;padding:0;box-sizing:border-box}
html,body{width:1200px;height:838px;overflow:hidden;background:var(--stage)}
body{position:relative;font-family:"Open Sans",sans-serif;color:var(--white)}
.page{position:absolute;top:30px;height:752px;overflow:hidden}
.page--front{left:41px;width:533px;background:linear-gradient(180deg,#0f2f44 60%,var(--teal-dark) 72%,var(--slate) 100%)}
.page--back{left:614px;width:514px;background:var(--navy)}
.abs{position:absolute}
.ph{position:absolute}
/* front */
.hero{left:0;top:0;width:533px;height:338px;background:radial-gradient(circle at 20% 25%,#7a5a3a 0%,#3a2c24 30%,#15161a 70%)}
.site-url{right:14px;top:8px;font-size:15px;font-weight:400}
.logo{left:178px;top:70px;width:143px;height:58px;background:var(--white);border:3px solid #111;display:flex;align-items:center;gap:6px;padding:0 6px}
.logo__mark{width:12px;height:12px;background:var(--deep-blue);flex:none}
.logo__name{color:#111;font-size:13px;font-weight:600;line-height:1.1}
.band{left:0;width:533px;height:28px;background:rgba(30,70,100,.55)}
.headline{left:0;width:533px;top:140px;text-align:center;font-family:"Open Sans",sans-serif;font-weight:600;font-size:26px;line-height:31px;letter-spacing:.5px}
.tagline{left:0;width:533px;top:256px;text-align:center;font-style:italic;font-weight:700;font-size:22px}
.thumb{top:342px;height:124px}
.lead{left:10px;width:513px;top:474px;text-align:center;font-size:19px;line-height:23px}
.lead em{font-style:normal;font-weight:700;color:var(--light-blue)}
.quote{left:0;width:533px;top:572px;text-align:center;font-family:"Poppins",sans-serif;font-style:italic;font-weight:500;font-size:18.5px;line-height:23px}
.quote .mark{color:var(--accent-orange);font-weight:700;font-size:24px}
/* back */
.city{left:0;top:0;width:514px;height:335px;background:linear-gradient(180deg,#0a2d8a 0%,#1f5cd0 45%,#b6893c 72%,#1c3a68 100%)}
.title-band{left:0;top:290px;width:514px;height:48px;background:linear-gradient(180deg,rgba(20,60,120,.2),rgba(20,60,120,.75))}
.title{left:22px;top:298px;font-family:"Open Sans",sans-serif;font-style:italic;font-weight:700;font-size:22px;white-space:nowrap}
.title span{color:#2c4a7c}
.col{top:338px;height:174px;width:168px;background:linear-gradient(180deg,#0d2e5e,#1a4fa0);padding:8px 8px}
.col h3{font-family:"Open Sans",sans-serif;font-weight:600;font-size:11px;line-height:13px;margin-bottom:8px}
.col p{font-size:6.6px;line-height:8px}
.col .center{text-align:center}
.col ul{list-style:none;font-size:6.6px;line-height:12px}
.col li::before{content:"› ";color:var(--light-blue)}
.btn{position:absolute;left:8px;right:8px;bottom:10px;height:36px;border-radius:18px;background:var(--btn);text-align:center;padding-top:4px;box-shadow:0 2px 3px rgba(0,0,0,.4)}
.btn b{display:block;font-size:10px;font-weight:600}
.btn small{display:block;font-size:6px;line-height:7px}
.btn--single{height:22px;padding-top:5px;font-size:7.5px;font-weight:700}
.reviews{left:0;top:512px;width:514px;height:165px;background:var(--brand-blue)}
.reviews h2{position:absolute;left:0;width:514px;top:8px;text-align:center;font-family:"Poppins",sans-serif;font-weight:700;font-size:23px;letter-spacing:-.2px}
.card{top:584px;height:93px;background:var(--card-bg);color:var(--card-text);padding:6px 8px;border:2px solid #d7e3ee}
.card__head{display:flex;gap:5px;align-items:center;font-size:6.5px}
.card__avatar{width:16px;height:16px;background:#999;flex:none}
.card__head b{color:#3b5998}
.card__date{color:#888;font-size:5.5px}
.card__body{font-size:6.5px;line-height:9px;margin-top:6px}
.card__actions{position:absolute;left:8px;bottom:5px;font-size:6px;color:#6a7a90;display:flex;gap:26px}
.contact{left:0;top:677px;width:514px;height:76px;background:linear-gradient(180deg,#0c1e33,#173b63);text-align:center}
.contact h4{font-family:"Poppins",sans-serif;font-weight:500;font-size:18px;margin-top:7px}
.contact p{font-size:9px;font-weight:700;line-height:10px}
</style>
</head>
<body>

<section class="page page--front">
  <div class="ph hero" role="img" aria-label="Close-up photo of a photographer holding a camera in warm low light"></div>
  <div class="abs site-url">www.lakesidelensguild.com</div>
  <div class="abs logo"><span class="logo__mark"></span><span class="logo__name">Lakeside Lens Guild</span></div>
  <div class="abs band" style="top:140px"></div>
  <div class="abs band" style="top:176px"></div>
  <div class="abs band" style="top:212px"></div>
  <h1 class="abs headline">LEARN<br>PROFESSIONAL<br>PHOTOGRAPHY</h1>
  <p class="abs tagline">Ready to kick-start your photography?</p>
  <div class="ph thumb" style="left:0;width:158px;background:linear-gradient(180deg,#3d3f45,#6b6a4a 55%,#3f5a2a)" role="img" aria-label="Country road under a moonlit sky"></div>
  <div class="ph thumb" style="left:161px;width:196px;background:linear-gradient(180deg,#1a1a1a,#9a9a9a 55%,#2a2a2a)" role="img" aria-label="Black and white photo of a lakeside building at night"></div>
  <div class="ph thumb" style="left:360px;width:173px;background:linear-gradient(180deg,#1e5fc8,#5a8ad0 45%,#a8773a 80%,#3a3a4a)" role="img" aria-label="City waterfront at dusk seen from a lit stairway"></div>
  <p class="abs lead">Photography courses and workshops to suit all levels of skill and experience, in central <em>Geneva /Switzerland.</em></p>
  <p class="abs quote"><span class="mark">“</span>Start taking better pictures immediately<span class="mark">”</span><br>We don’t lose time on theory, we just<br>show you how to do it</p>
</section>

<section class="page page--back">
  <div class="ph city" role="img" aria-label="Geneva lakefront at night with the water jet and lit buildings"></div>
  <div class="abs title-band"></div>
  <h2 class="abs title">DIGITAL PHOTOGRAPHY <span>Courses for all levels</span></h2>

  <div class="abs col" style="left:0">
    <h3>Intensive photography courses for beginers</h3>
    <p>A 7 hours DSLR photography course aimed at total beginners with extended hands-on activities. The first 4 hours, we will give you all the practical knowledge you need with concrete examples. In the second part, we will practice together all the concepts that we have learned and review your work.</p>
    <div class="btn"><b>Choose this class if</b><small>You want to see a significant improvement<br>on your photography immediately.</small></div>
  </div>
  <div class="abs col" style="left:173px">
    <h3>Weekend photography classes for beginers</h3>
    <p class="center"><b style="font-size:8px">Our ultimate recommendation:</b></p>
    <p class="center" style="margin-top:6px">A total 10 hours photography course that takes place over 5 weeks after work, aimed at busy professionals. Every week we meet for two hours to go through key concepts, then give interesting and challenging assignments to review the results next week.</p>
    <div class="btn"><b>Choose this class if</b><small>You love photography and would love to<br>focus on it during five weeks to<br>make a serious improvement.</small></div>
  </div>
  <div class="abs col" style="left:346px">
    <h3>Other photography courses for all level</h3>
    <ul>
      <li>Half-day Course for Beginners</li>
      <li>Intermediate Photography Course</li>
      <li>Street Photography Course</li>
      <li>Portrait &amp; Studio Lighting Course</li>
      <li>Lightroom for Photographers Course</li>
      <li>Photoshop for Photographers Course</li>
      <li>Night and Low Light Photography Course</li>
      <li>One to One Private Courses</li>
    </ul>
    <div class="btn btn--single">Photography Gift Vouchers</div>
  </div>

  <div class="abs reviews"><h2>WE GOT GREAT REVIEWS BY OUR CUSTOMER</h2></div>
  <div class="abs card" style="left:14px;width:310px">
    <div class="card__head"><span class="card__avatar"></span><div><b>Maren Holloway</b> reviewed Lakeside Lens Guild<div class="card__date">November 23 at 10:12am</div></div></div>
    <p class="card__body">An excellent way to bond with your camera and to learn all its little quirks and how to convert them to your benefit. A day well spent with much useful information gained. Thank you!!</p>
    <div class="card__actions"><span>Like</span><span>Comment</span><span>Share</span></div>
  </div>
  <div class="abs card" style="left:329px;width:172px">
    <div class="card__head"><span class="card__avatar"></span><div><b>Lena Vorberg</b> reviewed Lakeside Lens Guild<div class="card__date">July 24</div></div></div>
    <p class="card__body">Excellent training, friendly teacher, all the basics you need to know to master your camera. Loved it! Highly recommended!</p>
    <div class="card__actions"><span>Like</span><span>Comment</span><span>Share</span></div>
  </div>

  <div class="abs contact">
    <h4>For further information please contact us</h4>
    <p>CONTACT US NOW : +41 79 555 01 23<br>OR<br>VISIT OUR WEBSITE FOR MORE INFORMATION<br>www.lakesidelensguild.com</p>
  </div>
</section>

</body>
</html>
```